Brixel Information Technology Solutions
We are an Information Technology Company. We provide computer services to commercial companies. We would like a new card full color front and back with bleeding edge.
We have a logo that you can use or if you want to come up with a new logo that is fine too.
Our colors are mostly Maroon and black but be creative.
Sample Information
Grant P Oswick
4818 W Saguaro Ridge Drive
Suite 410
Phoenix, AZ 85016
O: 602.555.0143
C: 602.555.0178
24/7: 888.555.0162
goswick@brixelit.com
www.brixelit.com
Target Market(s)
Business of all sizes
Industry/Entity Type
Computer
Requirements
Must have
- Bleeding edge
full color on both sides

```html
<!DOCTYPE html>
<html lang="en">
<head>
<meta charset="utf-8">
<title>Brixel Information Technology Solutions – Business Card</title>
<link rel="stylesheet" href="https://fonts.googleapis.com/css2?family=Open+Sans:wght@700&family=Roboto:wght@700&family=Roboto+Condensed:wght@400&display=swap">
<style>
  :root {
    --backdrop: #858585;
    --card-white: #ffffff;
    --card-mist: #dcdcdc;
    --maroon: #b5222b;
    --maroon-deep: #7e1016;
    --maroon-light: #c9333b;
    --ink-gray: #58595b;
    --tag-gray: #6d6e70;
    --text-white: #ffffff;
  }
  * { margin: 0; padding: 0; box-sizing: border-box; }
  html, body { width: 1200px; height: 900px; overflow: hidden; }
  body { background: var(--backdrop); position: relative; }

  .card {
    position: absolute;
    overflow: hidden;
    border-radius: 4px;
    box-shadow: 0 6px 18px rgba(0,0,0,.35);
    background: radial-gradient(ellipse at 35% 20%, var(--card-white) 0%, var(--card-white) 40%, var(--card-mist) 100%);
  }
  .card-front { left: 80px; top: 50px; width: 840px; height: 480px; }
  .card-back  { left: 660px; top: 590px; width: 480px; height: 274px; }

  .card-art { position: absolute; inset: 0; width: 100%; height: 100%; }

  .brand-name {
    font-family: "Roboto", Arial, sans-serif;
    font-weight: 700;
    color: var(--ink-gray);
    letter-spacing: 0.12em;
    line-height: 1;
  }
  .brand-tagline {
    font-family: "Roboto Condensed", "Arial Narrow", sans-serif;
    color: var(--tag-gray);
    line-height: 1;
  }

  .card-front .brand { position: absolute; left: 52px; top: 44px; }
  .card-front .brand-name { font-size: 62px; }
  .card-front .brand-tagline { font-size: 25px; margin-top: 8px; }

  .holder-name {
    position: absolute; left: 52px; top: 168px;
    font-family: "Open Sans", Arial, sans-serif; font-weight: 700;
    font-size: 38px; line-height: 1.2; color: var(--maroon);
  }

  .address, .contact {
    position: absolute;
    font-family: "Open Sans", Arial, sans-serif; font-weight: 700;
    color: var(--text-white); list-style: none;
    line-height: 1;
  }
  .address { left: 52px; top: 318px; font-size: 23px; }
  .address li + li { margin-top: 22px; }
  .contact { right: 40px; top: 200px; text-align: right; font-size: 20px; }
  .contact li + li { margin-top: 21px; }

  .card-back .brand { position: absolute; left: 66px; top: 88px; }
  .card-back .brand-name { font-size: 50px; }
  .card-back .brand-tagline { font-size: 20px; margin-top: 8px; }
</style>
</head>
<body>

<section class="card card-front" aria-label="Business card front">
  <svg class="card-art" viewBox="0 0 840 480" preserveAspectRatio="none" role="img" aria-label="Decorative maroon and black swoosh artwork area">
    <defs>
      <linearGradient id="maroonFill" x1="0" y1="0" x2="0.3" y2="1">
        <stop offset="0" stop-color="var(--maroon-light)"/>
        <stop offset="0.45" stop-color="var(--maroon)"/>
        <stop offset="1" stop-color="var(--maroon-deep)"/>
      </linearGradient>
    </defs>
    <path class="maroon-panel" d="M0,300 C420,300 620,200 840,40 L840,480 L0,480 Z" fill="url(#maroonFill)"/>
  </svg>

  <div class="brand">
    <p class="brand-name">BRIXEL</p>
    <p class="brand-tagline">Information Technology Solutions</p>
  </div>

  <h1 class="holder-name">Grant P Oswick</h1>

  <ul class="address">
    <li>4818 W Saguaro Ridge Drive</li>
    <li>Suite 410</li>
    <li>Phoenix, AZ 85016</li>
  </ul>

  <ul class="contact">
    <li>O: 602.555.0143</li>
    <li>C: 602.555.0178</li>
    <li>24/7: 888.555.0162</li>
    <li>goswick@brixelit.com</li>
    <li>www.brixelit.com</li>
  </ul>
</section>

<section class="card card-back" aria-label="Business card back">
  <div class="brand">
    <p class="brand-name">BRIXEL</p>
    <p class="brand-tagline">Information Technology Solutions</p>
  </div>
</section>

</body>
</html>
```